Business Card Design

We sell fish products to corporate food companies who then turn these products into final food products for consumers

Industry/Entity Type

Business

Contact Information for Business Card

I need a corporate business card template for a fish products business. We would like it be professional for use in dealing with multi national companies. This company business card template will be used by multiple employees so the following fields must be open to edit (Name, Phone Number and Email address)

```html
<!DOCTYPE html>
<html lang="en">
<head>
<meta charset="utf-8">
<title>Coral Bay Seafoods – Business Card</title>
<link rel="stylesheet" href="https://fonts.googleapis.com/css2?family=Roboto:wght@300;400;700&display=swap">
<style>
  :root {
    --page-bg: #e6e6e4;
    --card-light: #dce9ec;
    --wave-deep: #2a62b0;
    --wave-mid: #3a78c2;
    --wave-glow: #5b96d0;
    --brand-blue: #2f66ae;
    --brand-dot: #3aa0c8;
    --text-white: #ffffff;
  }
  * { margin: 0; padding: 0; box-sizing: border-box; }
  html, body {
    width: 1200px;
    height: 1000px;
    overflow: hidden;
    background: var(--page-bg);
    font-family: "Roboto", Arial, sans-serif;
  }
  .canvas {
    width: 1200px;
    height: 1000px;
    display: flex;
    align-items: center;
    justify-content: center;
  }
  .business-card {
    position: relative;
    width: 900px;
    height: 514px;
    background: var(--card-light);
    overflow: hidden;
    box-shadow: 0 10px 30px rgba(0,0,0,0.15);
  }
  .wave-band {
    position: absolute;
    inset: 0;
    width: 100%;
    height: 100%;
  }
  .brand {
    position: absolute;
    top: 58px;
    right: 56px;
    display: flex;
    align-items: center;
    gap: 14px;
  }
  .brand-dot {
    width: 46px;
    height: 46px;
    border-radius: 50%;
    background: var(--brand-dot);
  }
  .brand-name {
    font-weight: 400;
    font-size: 36px;
    letter-spacing: 1px;
    color: var(--brand-blue);
    text-transform: uppercase;
    line-height: 1;
  }
  .contact {
    position: absolute;
    left: 120px;
    top: 330px;
    color: var(--text-white);
  }
  .contact-name {
    font-weight: 300;
    font-size: 40px;
    letter-spacing: 1px;
    text-transform: uppercase;
    line-height: 1;
  }
  .contact-role {
    font-weight: 700;
    font-size: 21px;
    margin-top: 2px;
    margin-left: 22px;
  }
  .contact-lines {
    list-style: none;
    margin-top: 10px;
    margin-left: 46px;
    font-weight: 300;
    font-size: 18px;
    line-height: 1.5;
  }
  .contact-lines li {
    display: flex;
    align-items: center;
    gap: 10px;
  }
  .contact-icon {
    width: 13px;
    height: 13px;
    fill: var(--text-white);
    flex: none;
  }
</style>
</head>
<body>
<main class="canvas">
  <section class="business-card">
    <svg class="wave-band" viewBox="0 0 900 514" preserveAspectRatio="none" aria-hidden="true">
      <defs>
        <linearGradient id="waveFill" x1="0" y1="1" x2="1" y2="0">
          <stop offset="0" stop-color="var(--wave-deep)"/>
          <stop offset="0.55" stop-color="var(--wave-mid)"/>
          <stop offset="0.75" stop-color="var(--wave-glow)"/>
          <stop offset="1" stop-color="var(--wave-mid)"/>
        </linearGradient>
      </defs>
      <path d="M0,170 C170,270 360,330 520,300 C680,270 800,170 900,70 L900,514 L0,514 Z" fill="url(#waveFill)"/>
    </svg>

    <div class="brand">
      <span class="brand-dot"></span>
      <span class="brand-name">Coral Bay Seafoods</span>
    </div>

    <div class="contact">
      <h1 class="contact-name">Jane Doe</h1>
      <p class="contact-role">General Manager</p>
      <ul class="contact-lines">
        <li>
          <svg class="contact-icon" viewBox="0 0 16 16" aria-hidden="true"><path d="M1 3h14v10H1z M1 3l7 6 7-6" fill="none" stroke="#fff" stroke-width="1.6"/></svg>
          <span class="contact-email">JaneDoe@coralbayseafoods.com</span>
        </li>
        <li>
          <svg class="contact-icon" viewBox="0 0 16 16" aria-hidden="true"><path d="M4 1l3 3-2 2c1 2 3 4 5 5l2-2 3 3-2 3C7 15 1 9 1 3z"/></svg>
          <span class="contact-phone">+ 0000 000 0000</span>
        </li>
      </ul>
    </div>
  </section>
</main>
</body>
</html>
```